Harrowgate Supply Group Business Card Design

The Business Card will be one side only with Harrowgate Supplies Group Logo
Card should have:
Name
Title
Office phone Number
Cell Number
email address
Website
Street Address
Our Slogan is Rugged and Reliable
Looking for something that stands out from other business cards

Target Market(s)

Heavy equipment Lease Company

```html
<!DOCTYPE html>
<html lang="en">
<head>
<meta charset="utf-8">
<title>Harrowgate Supplies Group – Business Card</title>
<link href="https://fonts.googleapis.com/css2?family=Open+Sans:wght@400;600;700&display=swap" rel="stylesheet">
<style>
  :root {
    --navy: #262a7a;
    --red: #d6123a;
    --ink: #4a4a4a;
    --rule: #9a9a9a;
    --paper: #ffffff;
    --backdrop: #e4e4e2;
  }
  * { margin: 0; padding: 0; box-sizing: border-box; }
  html, body {
    width: 1200px; height: 862px; overflow: hidden;
    background: var(--backdrop);
    font-family: "Open Sans", Arial, sans-serif;
  }
  .card {
    position: absolute; left: 100px; top: 145px;
    width: 1000px; height: 572px;
    background: var(--paper);
    box-shadow: 0 10px 30px rgba(0,0,0,.18);
    overflow: hidden;
  }
  .brand {
    position: absolute; left: 430px; top: 120px;
    display: flex; align-items: center; gap: 14px;
  }
  .brand-square { width: 26px; height: 26px; background: var(--red); }
  .brand-name {
    color: var(--red); font-weight: 700; font-size: 34px;
    letter-spacing: .5px; text-transform: uppercase;
  }
  .divider {
    position: absolute; left: 110px; right: 40px; top: 288px;
    height: 1px; background: var(--rule);
  }
  .address {
    position: absolute; right: 45px; top: 305px;
    text-align: right; color: var(--ink); font-size: 21px; line-height: 31px;
  }
  .person { position: absolute; left: 110px; top: 360px; }
  .person-name { color: var(--navy); font-weight: 700; font-size: 30px; line-height: 34px; }
  .person-title { color: var(--red); font-size: 21px; line-height: 28px; text-transform: uppercase; }
  .side-tab {
    position: absolute; left: 0; top: 392px; width: 30px; height: 52px;
    background: var(--navy);
  }
  .contacts { position: absolute; left: 130px; top: 440px; list-style: none; }
  .contacts li {
    display: flex; align-items: center; gap: 14px;
    color: var(--ink); font-size: 21px; line-height: 31px;
  }
  .contacts svg { width: 20px; height: 20px; fill: var(--navy); flex: none; }
  .bands { position: absolute; left: 0; bottom: 0; width: 1000px; height: 70px; }
  .slogan {
    position: absolute; right: 40px; bottom: 12px;
    color: #fff; font-weight: 700; font-size: 22px; letter-spacing: .5px;
  }
</style>
</head>
<body>
  <div class="card">
    <div class="brand">
      <span class="brand-square"></span>
      <span class="brand-name">Harrowgate Supplies Group</span>
    </div>

    <div class="divider"></div>

    <address class="address" style="font-style:normal">
      2710 Ridgeline Avenue<br>
      Brookvale, NY 11990<br>
      www.harrowgatesupplies.com
    </address>

    <div class="side-tab"></div>
    <div class="person">
      <div class="person-name">MILES CARROW</div>
      <div class="person-title">President</div>
    </div>

    <ul class="contacts">
      <li>
        <svg viewBox="0 0 24 24"><path d="M6.6 10.8a15 15 0 0 0 6.6 6.6l2.2-2.2c.3-.3.7-.4 1-.2 1.1.4 2.3.6 3.6.6.6 0 1 .4 1 1V20c0 .6-.4 1-1 1A17 17 0 0 1 3 4c0-.6.4-1 1-1h3.5c.6 0 1 .4 1 1 0 1.3.2 2.5.6 3.6.1.3 0 .7-.2 1z"/></svg>
        555 0142 7781
      </li>
      <li>
        <svg viewBox="0 0 24 24"><path d="M7 1h10a2 2 0 0 1 2 2v18a2 2 0 0 1-2 2H7a2 2 0 0 1-2-2V3a2 2 0 0 1 2-2zm0 3v14h10V4zm5 15.5a1 1 0 1 0 0 2 1 1 0 0 0 0-2z"/></svg>
        555 0198 3364
      </li>
      <li>
        <svg viewBox="0 0 24 24"><path d="M2 5h20v14H2zm2 2v.5l8 5 8-5V7zm0 3v7h16v-7l-8 5z"/></svg>
        miles@harrowgatesupplies.com
      </li>
    </ul>

    <svg class="bands" viewBox="0 0 1000 70" preserveAspectRatio="none">
      <polygon points="0,56 660,56 646,70 0,70" fill="var(--red)"/>
      <polygon points="650,12 1000,12 1000,70 606,70" fill="var(--navy)"/>
    </svg>
    <div class="slogan">Rugged and Reliable</div>
  </div>
</body>
</html>
```